Psychology service brochure

Marketing brochure for a new psychological counselling service.
Our old brochure was too boring and conservative. We are selling our services to GP's, psychiatrists, other health providers and of course potential clients. We'd really like a professional, elegant look that conveys us to be compassionate and conscientious providers of psychological services.
I have included a copy of our old brochure and a copy of the changes we'd like to the text.
Updates
I have included a photo of myself and my business partner. Only the faces are needed, so backgrounds would need to be edited out.
Hello, in consultation with my business partner, we would like
the use of our photos in the brochure please (with backgrounds edited out)
no stock photos of random people
use of abstract or nature/floral motifs suggestive of tranquillity
regards,
Miriam
Target Market(s)
General practitioner doctors, potential clients
Industry/Entity Type
Health
Requirements
Must have
- must include BlairMdITC TT- font for the business name
- must include our signature color Pantone 291 (see attached brochure)
- use of the photos of myself and my business partner (with background edited out please)
- keep use of colours to a minimum, 3 colors maximum, one of which must be Pantone 291
- must include changes to the brochure as outlined in the 'Changes to Pamphlet' document.
Nice to have
- an interesting, eye catching layout.
- interesting use of white spaces
- use of subtle abstract or nature/floral related graphics suggestive of tranquillity
Should not have
- should not include our fee
- stock photos of people

```html
<!DOCTYPE html>
<html lang="en">
<head>
<meta charset="utf-8">
<title>Quiet Harbour Counselling – Practitioners and Fees</title>
<link rel="stylesheet" href="https://fonts.googleapis.com/css2?family=Open+Sans:wght@300;400&display=swap">
<style>
  :root {
    --paper: #dcdcdc;
    --brand-blue: #3d9ad8;
    --brand-deep: #1876c4;
    --mark-light: #c9dbe8;
  }
  * { margin: 0; padding: 0; box-sizing: border-box; }
  html, body {
    width: 1200px; height: 900px; overflow: hidden;
    background: var(--paper);
  }
  .brochure-spread {
    position: relative; width: 1200px; height: 900px;
    font-family: "Open Sans", "Helvetica Neue", Arial, sans-serif;
    font-weight: 300; color: var(--brand-blue);
  }
  .panel {
    position: absolute; top: 0; width: 300px; height: 900px;
  }
  .panel--left { left: 58px; }
  .panel--middle { left: 455px; width: 298px; }
  .panel--right { left: 838px; }
  .panel-heading {
    text-align: center; font-size: 15px; line-height: 20px; font-weight: 300;
  }
  .panel--left .panel-heading { margin-top: 90px; }
  .panel--middle .panel-heading { margin-top: 91px; }
  .panel--right .panel-heading { margin-top: 112px; }
  .panel-body { margin-top: 20px; }
  .panel--right .panel-body { margin-top: 20px; }
  .panel-body p {
    font-size: 15px; line-height: 20px; text-align: justify;
    hyphens: auto; -webkit-hyphens: auto; margin-bottom: 20px;
  }
  .panel-body p.fee-notice {
    color: var(--brand-deep); font-size: 15.5px; font-weight: 400;
  }
  .practice-signoff {
    position: absolute; top: 800px;
    display: flex; align-items: center; gap: 8px;
  }
  .practice-signoff--left { left: 25px; }
  .practice-signoff--middle { left: 428px; }
  .practice-signoff--right { left: 823px; }
  .signoff-square { width: 28px; height: 28px; display: block; }
  .signoff-name {
    font-family: "Open Sans", "Helvetica Neue", Arial, sans-serif;
    font-weight: 400; font-size: 12px; letter-spacing: 1.5px;
    text-transform: uppercase; color: var(--brand-blue);
  }
</style>
</head>
<body>
<main class="brochure-spread">

  <section class="panel panel--left">
    <h2 class="panel-heading">Miriam Hale<br>Clinical Psychologist<br>M.Psych (Clin.) MAPS</h2>
    <div class="panel-body">
      <p>Miriam is a Clinical Psychologist with fifteen years of experience providing a range of psychological services to challenging clients within the public mental health sector including forensic, addiction and dual diagnosis services. She has been employed as a Senior Psychologist in this capacity for the last seven years.</p>
      <p>Miriam is a trained and experienced Cognitive Behavioural Therapist and is skilled in treating individuals and groups with a range of mood disorders including anxiety, depression and panic disorder, as well as in helping clients to overcome life issues such as grief and loss, stress management and anger management and is eligible to provide Pregnancy Support Counselling services under Medicare.</p>
      <p>Miriam trains other mental health clinicians and university students in treatment modalities including Motivational Interviewing and Brief Interventions. She has an interest in brain-based research into neuroplasticity and it’s application to cognitive therapy and change.</p>
    </div>
  </section>

  <section class="panel panel--middle">
    <h2 class="panel-heading">Helena Marsh<br>Clinical Psychologist<br>M.Psych (Clin.) MAPS</h2>
    <div class="panel-body">
      <p>Helena is a Clinical Psychologist, and with 15 years experience working in the public health sector, seven as a Senior Psychologist, she is a highly skilled clinician in the areas of mental health, addiction and dual diagnosis.</p>
      <p>She has more recently specialised in working with adolescents but has significant experience treating adults, both individually and in a variety of group programmes. She has also facilitated numerous training events and mentored clinicians in addressing dual diagnosis issues with their clients.</p>
      <p>Helena primarily utilises a Cognitive Behavioural framework and Motivational Interviewing, and has a special interest in working with adolescents who are experiencing developmental difficulties, antenatal and post-natal depression/stress, and parenting issues.</p>
      <p>Additionally Helena is skilful working in the areas of grief &amp; loss, life transition and adjustment issues, relationship and interpersonal challenges, and personal development.</p>
    </div>
  </section>

  <section class="panel panel--right">
    <h2 class="panel-heading">Our Fee Structure</h2>
    <div class="panel-body">
      <p>The practice accepts referrals from self-referring individuals, as well as from health professionals such as GPs, Psychiatrists, and Maternal and Child Health Nurses.</p>
      <p>Medicare rebates are available for clients referred for treatment by their GP.</p>
      <p>There are different tiers of rebates for Psychologists under Medicare, and this is dependent on treatment received (individual, group or pregnancy support counselling), and whether you are treated by a Psychologist or a Clinical Psychologist.</p>
      <p>Please contact us directly to further discuss fees for treatment.</p>
      <p>Fees are paid in full at the end of each session, and a receipt is provided which will allow you to obtain your refund at any Medicare office.</p>
      <p class="fee-notice">The practice does not bulk bill at this time, but we anticipate the addition of this facility in the future.</p>
    </div>
  </section>

  <footer class="practice-signoff practice-signoff--left">
    <svg class="signoff-square" viewBox="0 0 28 28" aria-hidden="true"><rect width="28" height="28" fill="var(--brand-blue)"/></svg>
    <span class="signoff-name">Quiet Harbour Counselling</span>
  </footer>
  <footer class="practice-signoff practice-signoff--middle">
    <svg class="signoff-square" viewBox="0 0 28 28" aria-hidden="true"><rect width="28" height="28" fill="var(--brand-blue)"/></svg>
    <span class="signoff-name">Quiet Harbour Counselling</span>
  </footer>
  <footer class="practice-signoff practice-signoff--right">
    <svg class="signoff-square" viewBox="0 0 28 28" aria-hidden="true"><rect width="28" height="28" fill="var(--brand-blue)"/></svg>
    <span class="signoff-name">Quiet Harbour Counselling</span>
  </footer>

</main>
</body>
</html>
```